The Quick Guard Privacy Handbook

A book cover. The book will be marketed as a promotional item for financial advisors, financial planners, independent insurance agents, bankers, and any professional who views their role as guardian of their clients assets and helping them manage risk.

```html
<!DOCTYPE html>
<html lang="en">
<head>
<meta charset="utf-8">
<title>The Quick Guard Privacy Handbook</title>
<link href="https://fonts.googleapis.com/css2?family=Roboto:ital,wght@0,400;0,500;0,700;0,900;1,500&family=Roboto+Condensed:wght@700&display=swap" rel="stylesheet">
<style>
  :root {
    --navy-top: #1b3263;
    --navy-deep: #122550;
    --gold: #e7ae2f;
    --gold-soft: #f0c25a;
    --white: #ffffff;
    --sky-mid: #4f7fb6;
    --sky-light: #a9c6e3;
    --sun: #f6c477;
    --horizon: #e9953a;
    --rock: #2a2f3a;
    --rock-deep: #121827;
  }
  html, body {
    margin: 0;
    padding: 0;
    width: 800px;
    height: 1200px;
    overflow: hidden;
    background: #1a1a1a;
  }
  .cover {
    position: relative;
    width: 800px;
    height: 1200px;
    overflow: hidden;
    background: linear-gradient(180deg, var(--navy-deep) 0%, var(--navy-top) 40%, var(--navy-top) 100%);
    font-family: "Roboto", sans-serif;
    color: var(--white);
    text-align: center;
  }
  .scene {
    position: absolute;
    left: 0;
    right: 0;
    top: 430px;
    bottom: 0;
    background: linear-gradient(180deg,
      rgba(27, 50, 99, 0) 0%,
      var(--sky-mid) 22%,
      var(--sky-light) 38%,
      var(--sun) 50%,
      var(--horizon) 54%,
      #5c6a80 58%,
      var(--rock) 66%,
      var(--rock-deep) 82%,
      #0e1424 100%);
  }
  .content {
    position: relative;
    z-index: 1;
  }
  .crest-row {
    position: absolute;
    top: 62px;
    left: 70px;
    right: 70px;
    display: flex;
    align-items: center;
    justify-content: center;
    gap: 26px;
  }
  .crest-row .rule {
    flex: 1;
    height: 2px;
    background: var(--gold);
  }
  .crest-mark {
    width: 60px;
    height: 60px;
    border-radius: 50%;
    border: 3px solid var(--gold);
    box-sizing: border-box;
  }
  .title {
    position: absolute;
    top: 178px;
    left: 0;
    right: 0;
    margin: 0;
    font-weight: 700;
    line-height: 1;
  }
  .title .lead {
    display: block;
    font-family: "Roboto Condensed", sans-serif;
    font-size: 68px;
    letter-spacing: -0.5px;
  }
  .title .main {
    display: block;
    font-size: 92px;
    letter-spacing: -1.5px;
    margin-top: 12px;
  }
  .subtitle {
    position: absolute;
    top: 492px;
    left: 0;
    right: 0;
    margin: 0;
    font-style: italic;
    font-weight: 500;
    font-size: 27px;
    line-height: 1.45;
    color: var(--gold-soft);
  }
  .divider {
    position: absolute;
    top: 590px;
    left: 260px;
    width: 280px;
    height: 14px;
    display: flex;
    align-items: center;
    gap: 12px;
  }
  .divider .rule { flex: 1; height: 2px; background: var(--gold); }
  .divider .gem {
    width: 10px; height: 10px;
    background: var(--gold);
    transform: rotate(45deg);
  }
  .motto {
    position: absolute;
    top: 622px;
    left: 0;
    right: 0;
    margin: 0;
    font-size: 16px;
    letter-spacing: 1px;
    line-height: 1.55;
    text-transform: uppercase;
  }
  .pillars {
    position: absolute;
    top: 930px;
    left: 50px;
    right: 50px;
    display: flex;
    list-style: none;
    margin: 0;
    padding: 0;
  }
  .pillar {
    flex: 1;
    display: flex;
    flex-direction: column;
    align-items: center;
    gap: 10px;
    font-size: 14px;
    font-weight: 500;
    letter-spacing: 0.5px;
    line-height: 1.35;
    text-transform: uppercase;
    border-left: 1px solid rgba(231, 174, 47, 0.6);
  }
  .pillar:first-child { border-left: none; }
  .pillar svg { width: 62px; height: 62px; }
  .promise {
    position: absolute;
    top: 1078px;
    left: 0;
    right: 0;
    margin: 0;
    text-transform: uppercase;
    letter-spacing: 2px;
    line-height: 1.5;
  }
  .promise .small { display: block; font-size: 19px; color: var(--gold-soft); font-weight: 500; }
  .promise .large { display: block; font-size: 23px; font-weight: 700; }
  .base-rule {
    position: absolute;
    top: 1160px;
    left: 230px;
    width: 340px;
    height: 2px;
    background: var(--gold);
  }
</style>
</head>
<body>
<main class="cover">
  <div class="scene" role="img" aria-label="Photograph of a lighthouse on a rocky coast at sunset, with a family of four holding hands looking out at the sea"></div>

  <div class="content">
    <div class="crest-row">
      <span class="rule"></span>
      <span class="crest-mark" aria-hidden="true"></span>
      <span class="rule"></span>
    </div>

    <h1 class="title">
      <span class="lead">The Quick Guard</span>
      <span class="main">Privacy</span>
      <span class="main">Handbook</span>
    </h1>

    <p class="subtitle">Protect Yourself and Your Family<br>in the AI Age</p>

    <div class="divider"><span class="rule"></span><span class="gem"></span><span class="rule"></span></div>

    <p class="motto">It’s better to have it and not need it<br>than need it and not have it.</p>

    <ul class="pillars">
      <li class="pillar">
        <svg viewBox="0 0 62 62" aria-hidden="true">
          <path d="M31 4 L54 12 V30 C54 44 44 54 31 59 C18 54 8 44 8 30 V12 Z" fill="none" stroke="var(--gold)" stroke-width="3.5"/>
          <circle cx="31" cy="25" r="7" fill="var(--gold)"/>
          <path d="M19 45 C20 36 42 36 43 45 Z" fill="var(--gold)"/>
        </svg>
        <span>Protect<br>what matters</span>
      </li>
      <li class="pillar">
        <svg viewBox="0 0 62 62" aria-hidden="true">
          <path d="M20 28 V20 C20 8 42 8 42 20 V28" fill="none" stroke="var(--gold)" stroke-width="4"/>
          <rect x="13" y="28" width="36" height="28" rx="4" fill="none" stroke="var(--gold)" stroke-width="3.5"/>
          <circle cx="31" cy="40" r="4" fill="var(--gold)"/>
          <rect x="29.5" y="41" width="3" height="8" fill="var(--gold)"/>
        </svg>
        <span>Secure<br>your identity</span>
      </li>
      <li class="pillar">
        <svg viewBox="0 0 62 62" aria-hidden="true">
          <circle cx="14" cy="18" r="6" fill="var(--gold)"/>
          <circle cx="31" cy="14" r="7" fill="var(--gold)"/>
          <circle cx="48" cy="18" r="6" fill="var(--gold)"/>
          <rect x="8" y="27" width="12" height="28" rx="3" fill="var(--gold)"/>
          <rect x="24" y="24" width="14" height="32" rx="3" fill="var(--gold)"/>
          <rect x="42" y="27" width="12" height="28" rx="3" fill="var(--gold)"/>
        </svg>
        <span>Protect<br>your family</span>
      </li>
      <li class="pillar">
        <svg viewBox="0 0 62 62" aria-hidden="true" fill="none" stroke="var(--gold)" stroke-width="2.5" stroke-linecap="round">
          <path d="M14 44 C10 24 20 8 31 8 C44 8 52 20 50 38"/>
          <path d="M20 50 C16 32 22 16 31 16 C40 16 45 26 44 40"/>
          <path d="M26 54 C23 38 25 24 31 24 C37 24 38 34 37 48"/>
          <path d="M31 32 C32 42 31 50 32 56"/>
        </svg>
        <span>Stay ahead<br>of threats</span>
      </li>
      <li class="pillar">
        <svg viewBox="0 0 62 62" aria-hidden="true" fill="none" stroke="var(--gold)" stroke-width="3.5" stroke-linecap="round" stroke-linejoin="round">
          <rect x="9" y="12" width="44" height="42" rx="4"/>
          <path d="M9 24 H53"/>
          <path d="M20 6 V16 M42 6 V16"/>
          <path d="M21 39 L28 46 L41 32"/>
        </svg>
        <span>Plan today<br>for tomorrow</span>
      </li>
    </ul>

    <p class="promise">
      <span class="small">A small investment of time today.</span>
      <span class="large">A lifetime of peace of mind.</span>
    </p>

    <div class="base-rule"></div>
  </div>
</main>
</body>
</html>
```